Marketing Company Needs Creative Brochure Design

We need a brochure design for a new company based in the Twin Cities called 'Lanternway Marketing'. We work with our clients to get them found on the internet and at the top of Zorvex page rankings. We offer a variety of marketing tools for our clients from Search Engine Optimization (SEO), to social media, videos, blogs, article marketing, etc... We would like to incorporate the blacksmith theme. Our colors are red and black. The final design should communicate business growth.

Target Market(s)

business owners

Industry/Entity Type

Marketing

Requirements
Should not have
• Although we would like to incorporate the blacksmith theme, please don't make it cheesy. Think sophistication and creativity.

```html
<!DOCTYPE html>
<html lang="en">
<head>
<meta charset="utf-8">
<title>Lanternway Marketing – Inside Spread</title>
<link href="https://fonts.googleapis.com/css2?family=Open+Sans:ital,wght@0,400;0,600;0,700;0,800;1,300;1,400;1,600;1,700;1,800&display=swap" rel="stylesheet">
<style>
  :root{
    --red:#c4121d;
    --red-deep:#a50d16;
    --ink:#2a2a2a;
    --grey-text:#555;
    --paper:#ffffff;
    --stage:#e9e6e1;
  }
  *{box-sizing:border-box;margin:0;padding:0}
  html,body{width:1200px;height:522px;overflow:hidden;background:var(--stage);font-family:"Open Sans",Arial,sans-serif;color:var(--ink)}
  .spread{position:absolute;left:15px;top:26px;width:1170px;height:470px;background:var(--paper);box-shadow:0 2px 8px rgba(0,0,0,.25)}
  .panel{position:absolute;top:0;height:470px;overflow:hidden}
  .panel--left{left:0;width:376px}
  .panel--middle{left:376px;width:398px;border-left:1px dashed #888}
  .panel--right{left:774px;width:396px;border-left:1px dashed #888}
  .strip{position:absolute;left:0;right:0;bottom:0;height:18px;background:var(--red)}
  .photo{position:absolute}
  .icon-box{position:absolute;width:34px;height:34px;border:2px solid #fff;border-radius:4px}
  .icon-box svg{width:100%;height:100%}

  /* left panel */
  .photo--forge{left:0;top:18px;width:376px;height:244px;background:
    radial-gradient(circle at 35% 30%,#4f7fae 0,#1c3550 22%,transparent 30%),
    radial-gradient(circle at 70% 75%,#e0402a 0,#7a1508 20%,transparent 45%),
    linear-gradient(120deg,#1a1a1a 0%,#5a2a1c 45%,#2a0c08 70%,#101010 100%)}
  .mission{position:absolute;left:112px;top:120px;width:250px;color:#fff;font-weight:800;font-size:10.2px;line-height:1.25;text-transform:uppercase;letter-spacing:.1px}
  .photo--keys{left:0;top:272px;width:376px;height:180px;background:linear-gradient(160deg,#6a6a6c 0%,#3e3e40 50%,#262628 100%)}
  .confidence{position:absolute;left:0;top:286px;width:376px;text-align:center;color:#fff;font-style:italic;font-weight:700;font-size:13.5px;line-height:1.3}
  .confidence .accent{display:block;color:var(--red);font-weight:800;font-size:21px;line-height:1.1}
  .confidence-body{position:absolute;left:58px;top:356px;width:300px;color:#e8e8e8;font-size:7px;line-height:1.4}

  /* middle panel */
  .lead{position:absolute;left:18px;top:26px;font-style:italic;font-weight:300;font-size:23px;color:#333}
  .lead-big{position:absolute;right:14px;top:48px;font-style:italic;font-weight:700;font-size:46px;line-height:1;color:var(--red);letter-spacing:-.5px}
  .band{position:absolute;left:0;right:0;top:104px;height:112px;background:var(--red);color:#fff}
  .band .icon-box{left:18px;top:4px;width:26px;height:26px}
  .band-title{position:absolute;left:54px;top:7px;font-weight:700;font-size:15px;line-height:1.2}
  .band-copy{position:absolute;left:16px;top:34px;width:372px;font-size:6.3px;line-height:1.3}
  .band-copy b{font-weight:700;display:inline-block;margin-top:5px}
  .column{position:absolute;font-size:6.4px;line-height:1.36;color:var(--grey-text)}
  .column h3{font-style:italic;font-weight:700;font-size:10.5px;color:var(--red);margin-bottom:3px}
  .column .kicker{color:var(--red);font-weight:700;font-size:8px;line-height:1.2;text-transform:uppercase;margin-bottom:10px}
  .column ol,.column ul{list-style:none}
  .column ol li b{color:var(--red)}
  .column .sub{font-weight:700;color:#333;margin-top:6px}
  .col--video{left:18px;top:232px;width:170px}
  .col--web{left:200px;top:232px;width:184px}

  /* right panel */
  .photo--anvil{left:14px;top:18px;width:368px;height:82px;background:linear-gradient(100deg,#2a1a12 0%,#7a4a2c 40%,#b8865a 60%,#3a2418 100%)}
  .question{position:absolute;left:20px;top:62px;width:360px;color:#fff;font-style:italic;font-weight:700;font-size:12px;line-height:1.05;text-align:right;text-shadow:0 1px 2px rgba(0,0,0,.6)}
  .question .big{font-size:16px}
  .band--social{left:14px;right:0;top:104px;height:112px}
  .band--social .band-title{left:8px;top:5px;font-style:italic;font-size:10.5px}
  .band--social .band-copy{left:8px;top:24px;width:368px}
  .band--social .fact{font-weight:700;font-size:7.4px;line-height:1.3;margin-bottom:1px}
  .col--promo{left:16px;top:224px;width:172px}
  .col--more{left:200px;top:224px;width:182px}
  .photo--fire{left:14px;top:377px;width:368px;height:80px;background:
    radial-gradient(circle at 45% 55%,#f6c24a 0,#d8641a 20%,transparent 45%),
    linear-gradient(90deg,#1b1410 0%,#4a2614 50%,#1b1410 100%)}
  .url-tag{position:absolute;left:0;top:0}
  .url{position:absolute;right:22px;top:440px;color:var(--red);font-style:italic;font-weight:700;font-size:10px}
</style>
</head>
<body>
<div class="spread">

  <section class="panel panel--left">
    <div class="photo photo--forge" role="img" aria-label="Collage of the globe, a blacksmith's hands and flying sparks"></div>
    <div class="icon-box" style="left:196px;top:66px">
      <svg viewBox="0 0 34 34" fill="none" stroke="#fff" stroke-width="1.6"><path d="M17 7a7 7 0 0 0-4 12.7V23h8v-3.3A7 7 0 0 0 17 7z"/><path d="M14 26h6M15 28.5h4"/></svg>
    </div>
    <p class="mission">Lanternway Marketing is dedicated to helping businesses use powerful new online and mobile marketing platforms to get visibility, traffic, leads, customers and raving fans.</p>
    <div class="photo photo--keys" role="img" aria-label="Close-up of dark keyboard keys"></div>
    <p class="confidence">If you’re not confident potential customers are finding<br>your business online, we have the<span class="accent">solution for you!</span></p>
    <p class="confidence-body">By utilizing Search Engine Optimization services, social media marketing, web-based videos, and so much more, our knowledgeable team will help you plan and execute marketing strategies that really work. We build your online marketing program incrementally to control costs, incorporate all the elements for the most impactful effect and real results, and accomplish all this and more with zero extra work on your part.</p>
    <div class="strip"></div>
  </section>

  <section class="panel panel--middle">
    <p class="lead">Let us take your marketing to the</p>
    <p class="lead-big">next level!</p>
    <div class="band">
      <div class="icon-box">
        <svg viewBox="0 0 28 28" fill="none" stroke="#fff" stroke-width="1.5"><path d="M8 20l2-6 9-9 4 4-9 9z"/><path d="M8 20l6-2"/></svg>
      </div>
      <h2 class="band-title">OUR SERVICES</h2>
      <p class="band-copy">Our primary objectives are to build your online marketing program incrementally to control costs, integrate all the elements for the most powerful effect and greatest results and accomplish this with zero extra work on your part.<br>
      <b>Business Category:</b><br>Social Media Marketing, SEO, Marketing and Sales Consulting, Advertising Marketing, Website Design and Service<br>
      <b style="margin-top:0">Business Products:</b><br>Strategy &amp; planning, online video marketing programs, local directory marketing programs, mobile marketing programs, automated follow up systems and campaigns, lead capture systems and campaigns</p>
    </div>

    <article class="column col--video">
      <h3>Video</h3>
      <p class="kicker">Video is the most effective medium to showcase your business to the social media culture.</p>
      <p>Over 300 million people watch videos on Streamvale each month. These viewers share videos with their network of friends and family every day.<br>Make video work for your business! We offer high quality commercial grade videos that use specific keywords so you get the highest number of searches leading customers to find you. Our videos feature:</p>
      <ol>
        <li><b>1.</b> Full-fledged video production</li>
        <li><b>2.</b> Creative writing that will entice viewers to learn more about your business</li>
        <li><b>3.</b> Top of the line cinematography</li>
        <li><b>4.</b> Detailed, polished editing for videos that will wow viewers</li>
      </ol>
      <p>Plus, we will get your videos found by uploading them to a Streamvale channel for maximum exposure!</p>
    </article>

    <article class="column col--web">
      <h3>Web Presence</h3>
      <p class="kicker">Your company is a little fish in a big pond on the world wide web.</p>
      <p>Let us highlight your company and bring it to the surface. Our team is highly knowledgeable in Search Engine Optimization, or the craft of getting you listed high and on the front page of search results so that potential clients can find you. We use the best and most relevant keywords for your business, and we create a plan to optimize your site for these keywords. Search Engine Optimization is constantly evolving, and we are always working to stay ahead of the trends to provide the best service to our clients. When you appear higher in search results, a larger volume of people will visit your site and discover your business – it’s as simple as that. Your website is a powerful tool used to communicate with potential clients.</p>
      <p class="sub">Strategies</p>
      <ul><li>• Conduct Thorough Keyword Research</li></ul>
    </article>
    <div class="strip"></div>
  </section>

  <section class="panel panel--right">
    <div class="photo photo--anvil" role="img" aria-label="Blacksmith hammering glowing metal on an anvil"></div>
    <p class="question">Are you ready to put <span class="big">social media</span><br><span class="big">to work for your business?</span></p>
    <div class="band band--social">
      <h2 class="band-title">Social Media</h2>
      <div class="band-copy">
        <p class="fact">Fact: Chatterly and Quipster have more than 700 million combined members. Shouldn’t you connect with that audience?</p>
        <p>Social Media can help grow your business by leading people daily to what you have to offer. It is a critical part of SEO and internet marketing today, connecting you to a broad range of people who are interested in learning more about your brand, products and services. Our team of Social Media specialists employ the latest techniques available to generate buzz around your business in the social media world. We work with you to promote your brand through informative posts on a regular basis that aim to cast your net to a wider audience each day. We include backlinks to your site when posting, because research has shown that people love to click the live links provided in social media posts. This leads to more traffic to your website, and a greater number of potential clients. We set up and manage social media sites for you, such as Chatterly, Quipster and Linkwise.</p>
      </div>
    </div>

    <article class="column col--promo">
      <ul>
        <li>• Acquire Strategic Domain Name</li>
        <li>• Build Organic Search Results</li>
        <li>• Create Key Online Directories Profiles</li>
        <li>• Pay Per Click Campaign Management</li>
      </ul>
      <h3 style="margin-top:7px">Promotional Efforts</h3>
      <p>We’re in the business of promoting your business! We take professional photos of your company to enhance your online presence and give potential clients a face to your name. We create a blog that we populate for you with fresh content, allowing visitors to connect with you and share your insights with their network of friends. We write, distribute, and submit professional articles related to your field to an enormous</p>
    </article>

    <article class="column col--more">
      <p>database of directories. These articles include backlinks to your website, helping to push your site further up in Zorvex rankings. We also offer Spanish translation of these articles to maximize your impact on the web.<br>We take pride in the quality of our services. We install call tracking that lets you see how this specific internet marketing campaign has influenced the volume of calls your business receives, and we update you throughout the program with the most current analytics and ranking so you’ll always know where you stand.<br>We’d love to introduce your business to the thousands of potential clients online right now. If you’re ready to get started with and see your business grow with internet marketing, contact us today.</p>
    </article>

    <div class="photo photo--fire" role="img" aria-label="Glowing forge fire with hot metal"></div>
    <svg class="url-tag" width="396" height="470" viewBox="0 0 396 470" aria-hidden="true">
      <polygon points="210,432 396,424 396,458 200,458" fill="#fff"/>
    </svg>
    <p class="url">www.lanternwaymarketing.com</p>
  </section>

</div>
</body>
</html>
```